Coloring Book Cover | Unicorns

We are looking for a cover design for our new coloring book "Fox Garden Coloring Book - Lattice Pattern"
The target group are mostly female adults or girls aged 12+. The cover should have strong colors, associated with coloring unicorns (rainbow colors, pink, etc.).
The book is 8.5 x 11 inches.
Check out some of our other coloring books and their covers:
https://www.brimvale-market.de/gp/item/K7731TRW4Q
https://www.brimvale-market.de/gp/item/K7729PLM8D
The cover should have elements of the templates that are available inside the books. So feel free to check out the attached images and use one or more of them (or also just parts of one of the images).
The back of the cover should contain up to 4 bullets with the main advantages of the book. Check the given links to see how this looks on our other books.

Target Market(s)

Worldwide. Mostly females aged 12+

Requirements
Must have
• When the artwork is generated, the files we would like to receive are: The original working file PSD (Photoshop Document - so any text and images can be edited) All the working elements including: illustrations, photos, graphics and fonts A high resolution (300 dpi), 8.5 x 11 (or larger) file A JPG file in the exact size specifications and color required by our publisher

```html
<!DOCTYPE html>
<html lang="en">
<head>
<meta charset="utf-8">
<title>Fox Garden Coloring Book - Lattice Pattern · Cover</title>
<link href="https://fonts.googleapis.com/css2?family=Chewy&family=Caveat+Brush&display=swap" rel="stylesheet">
<style>
  :root {
    --stage: #ecebe8;
    --cover-dark: #2a2a2b;
    --cover-line: #3a3a3c;
    --gold: #b99a4a;
    --gold-text: #c4a75c;
    --panel: rgba(30, 26, 20, 0.78);
    --title-white: #f7f7f7;
    --pink: #e8306e;
    --magenta: #c01f8a;
    --lime: #7dea3a;
    --teal: #2fd8b5;
    --blue: #3a6cf0;
    --violet: #7a3de0;
    --yellow: #f2ea8a;
    --orange: #f08a3a;
  }
  * { box-sizing: border-box; margin: 0; padding: 0; }
  html, body {
    width: 1200px; height: 920px; overflow: hidden;
    background: var(--stage);
  }
  .spread { position: relative; width: 1200px; height: 920px; }
  .cover {
    position: absolute; top: 125px;
    width: 460px; height: 637px;
    background: var(--cover-dark);
    overflow: hidden;
  }
  .cover--back { left: 63px; }
  .cover--front { left: 650px; }

  .artwork { position: absolute; }

  /* back cover */
  .back-art {
    inset: 0;
    background:
      radial-gradient(circle at 78% 18%, var(--violet) 0 10%, transparent 22%),
      radial-gradient(ellipse at 72% 42%, var(--pink) 0 16%, transparent 34%),
      radial-gradient(ellipse at 55% 80%, var(--teal) 0 18%, transparent 40%),
      radial-gradient(ellipse at 85% 62%, var(--lime) 0 14%, transparent 36%),
      radial-gradient(ellipse at 12% 85%, var(--magenta) 0 8%, transparent 24%),
      radial-gradient(ellipse at 25% 40%, var(--blue) 0 6%, transparent 22%),
      var(--cover-dark);
  }
  .benefits {
    position: absolute; left: 122px; top: 203px;
    width: 215px; height: 280px;
    background: var(--panel);
    border: 4px solid var(--gold);
    display: flex; flex-direction: column; justify-content: space-around;
    align-items: center; padding: 14px 0;
    list-style: none;
  }
  .benefits li {
    font-family: "Chewy", cursive;
    font-size: 25px; color: var(--gold-text); letter-spacing: 0.5px;
  }

  /* front cover */
  .front-art-top {
    right: 0; top: 0; width: 460px; height: 190px;
    background:
      radial-gradient(circle at 88% 25%, var(--pink) 0 14%, var(--orange) 18%, transparent 30%),
      radial-gradient(circle at 90% 70%, var(--yellow) 0 12%, var(--blue) 20%, transparent 32%),
      radial-gradient(ellipse at 45% 0%, var(--lime) 0 8%, transparent 22%),
      radial-gradient(ellipse at 20% 0%, var(--violet) 0 10%, transparent 24%);
  }
  .front-art-unicorn {
    right: 0; top: 160px; width: 260px; height: 477px;
    background:
      radial-gradient(ellipse at 30% 35%, var(--pink) 0 18%, transparent 34%),
      radial-gradient(ellipse at 65% 25%, var(--teal) 0 16%, transparent 40%),
      radial-gradient(ellipse at 60% 75%, var(--yellow) 0 20%, var(--magenta) 32%, transparent 52%);
  }
  .front-art-bottom {
    left: 0; bottom: 0; width: 230px; height: 140px;
    background:
      radial-gradient(ellipse at 40% 90%, var(--magenta) 0 18%, var(--blue) 32%, transparent 55%),
      radial-gradient(ellipse at 55% 30%, var(--lime) 0 12%, transparent 36%);
  }
  .title {
    position: absolute; left: 18px; top: 78px;
    font-family: "Chewy", cursive;
    font-weight: 400; font-size: 64px; line-height: 82px;
    color: var(--title-white);
    text-shadow: 2px 3px 3px rgba(0,0,0,0.7);
    letter-spacing: 1px;
  }
  .subtitle {
    position: absolute; left: 20px; top: 322px;
    font-family: "Caveat Brush", cursive;
    font-size: 58px; line-height: 58px;
    background: linear-gradient(90deg, var(--blue), var(--violet));
    -webkit-background-clip: text; background-clip: text;
    color: transparent;
  }
</style>
</head>
<body>
<main class="spread">
  <section class="cover cover--back" aria-label="Back cover">
    <div class="artwork back-art" role="img" aria-label="Colourful lattice-pattern fox illustration with flowers and leaves in pink, green, blue and gold"></div>
    <ul class="benefits">
      <li>Lorem Ipsum</li>
      <li>Lorem Ipsum</li>
      <li>Lorem Ipsum</li>
      <li>Lorem Ipsum</li>
    </ul>
  </section>

  <section class="cover cover--front" aria-label="Front cover">
    <div class="artwork front-art-top" role="img" aria-label="Colourful round fruit and leaf ornaments along the top edge"></div>
    <div class="artwork front-art-unicorn" role="img" aria-label="Lattice-pattern fox illustration in pink, yellow and teal"></div>
    <div class="artwork front-art-bottom" role="img" aria-label="Colourful floral ornament in the lower corner"></div>
    <h1 class="title">Fox Garden<br>Coloring<br>Book</h1>
    <p class="subtitle">Lattice<br>Pattern</p>
  </section>
</main>
</body>
</html>
```